Looking for a clean, modern, and professional business card design that reflects Valtrin Systems

The design should include the company logo, contact details, and align with our brand identity. Please use a sophisticated and minimalist style, incorporating [specific colors, if applicable]. Creativity is welcome, but the card must maintain a polished and professional appearance.

Details to Include:

Name: Teo Barranzi
Title: VP Sales / Operations
Company: Valtrin Systems
Phone: 304.617.2285
Email: teo@valtrinsystems.example
Website: www.valtrinsystems.example

```html
<!DOCTYPE html>
<html lang="en">
<head>
<meta charset="utf-8">
<title>Valtrin Systems — Business Card</title>
<link href="https://fonts.googleapis.com/css2?family=Arimo:wght@400;700&display=swap" rel="stylesheet">
<style>
  :root {
    --stage: #e9e9ea;
    --card-white: #ffffff;
    --card-black: #1c1c1d;
    --pattern-dark: #262627;
    --ink: #111111;
    --ink-soft: #5a5a5a;
    --brand-blue: #3a78c2;
    --rule-blue: #7ea5d6;
  }
  * { box-sizing: border-box; margin: 0; padding: 0; }
  html, body {
    width: 1200px; height: 1108px; overflow: hidden;
    background: var(--stage);
    font-family: "Arimo", Arial, sans-serif;
  }
  .stage {
    position: relative; width: 1200px; height: 1108px;
    display: flex; justify-content: center; align-items: center; gap: 60px;
  }
  .card {
    position: relative; width: 420px; height: 720px; border-radius: 34px; overflow: hidden;
    box-shadow: 0 10px 30px rgba(0,0,0,.18);
  }
  .card--front { background: var(--card-white); }
  .card--back { background: var(--card-black); }

  .wordmark { text-align: center; font-weight: 700; line-height: 1; }
  .wordmark__name { display: block; font-size: 50px; letter-spacing: 2px; color: var(--ink); }
  .wordmark__sub { display: block; font-size: 16px; letter-spacing: 10px; color: var(--ink); margin-top: 8px; padding-left: 10px; }
  .card--front .wordmark { position: absolute; top: 96px; left: 0; right: 0; }

  .identity { position: absolute; top: 380px; left: 0; right: 0; text-align: center; }
  .identity__name { font-size: 30px; font-weight: 700; color: var(--ink); letter-spacing: .5px; }
  .identity__first { color: var(--brand-blue); }
  .identity__title { margin-top: 6px; font-size: 22px; color: var(--ink-soft); }

  .divider { position: absolute; top: 470px; left: 40px; right: 40px; display: flex; align-items: center; gap: 10px; }
  .divider__rule { flex: 1; height: 2px; background: var(--rule-blue); }
  .divider__icons { display: flex; gap: 8px; }
  .icon { width: 32px; height: 32px; border-radius: 6px; background: var(--brand-blue); display: flex; align-items: center; justify-content: center; }
  .icon svg { width: 20px; height: 20px; }

  .contact { position: absolute; top: 530px; left: 0; right: 0; text-align: center; font-size: 23px; color: var(--ink-soft); line-height: 1.4; }

  .back-texture { position: absolute; inset: 0; background: linear-gradient(135deg, var(--pattern-dark), var(--card-black) 60%, var(--pattern-dark)); }
  .card--back .wordmark { position: absolute; top: 50%; left: 0; right: 0; transform: translateY(-50%); }
  .card--back .wordmark__name, .card--back .wordmark__sub { color: #ffffff; }
  .card--back .wordmark__name { font-size: 40px; }
  .card--back .wordmark__sub { font-size: 13px; letter-spacing: 8px; }
</style>
</head>
<body>
<main class="stage">
  <section class="card card--front" aria-label="Card front">
    <div class="wordmark">
      <span class="wordmark__name">VALTRIN</span>
      <span class="wordmark__sub">SYSTEMS</span>
    </div>
    <div class="identity">
      <p class="identity__name"><span class="identity__first">TEO</span> BARRANZI</p>
      <p class="identity__title">VP Sales / Operations</p>
    </div>
    <div class="divider">
      <span class="divider__rule"></span>
      <span class="divider__icons">
        <span class="icon" aria-label="Phone"><svg viewBox="0 0 24 24"><path fill="#fff" d="M6.6 10.8a15 15 0 0 0 6.6 6.6l2.2-2.2a1 1 0 0 1 1-.25 11 11 0 0 0 3.6.6 1 1 0 0 1 1 1V20a1 1 0 0 1-1 1A17 17 0 0 1 3 4a1 1 0 0 1 1-1h3.5a1 1 0 0 1 1 1c0 1.25.2 2.45.6 3.6a1 1 0 0 1-.25 1z"/></svg></span>
        <span class="icon" aria-label="Email"><svg viewBox="0 0 24 24"><rect x="3" y="6" width="18" height="12" rx="1" fill="#fff"/><path d="M3.5 6.5 12 13l8.5-6.5" fill="none" stroke="#3a78c2" stroke-width="1.6"/></svg></span>
        <span class="icon" aria-label="Website"><svg viewBox="0 0 24 24"><circle cx="12" cy="12" r="8" fill="none" stroke="#fff" stroke-width="2"/><ellipse cx="12" cy="12" rx="3.5" ry="8" fill="none" stroke="#fff" stroke-width="1.6"/><path d="M4 12h16" stroke="#fff" stroke-width="1.6"/></svg></span>
      </span>
      <span class="divider__rule"></span>
    </div>
    <div class="contact">
      <p>304.617.2285</p>
      <p>teo@valtrinsystems.example</p>
      <p>www.valtrinsystems.example</p>
    </div>
  </section>

  <section class="card card--back" aria-label="Card back">
    <div class="back-texture" role="img" aria-label="Tone-on-tone repeating brand texture"></div>
    <div class="wordmark">
      <span class="wordmark__name">VALTRIN</span>
      <span class="wordmark__sub">SYSTEMS</span>
    </div>
  </section>
</main>
</body>
</html>
```